We will Buy your Home.

This is targeted to the homeowner that needs to sell their home fast. Our selling point is that "We will provide you with an offer to purchase your home in 24 hours Guarantee!" There is a 3 step process 1. Give us a call and provide us with your name and address. 2. One of our associates will give you a call to schedule a walk through of your property. 3. We will email you an offer to purchase within 24 hours of walking your property. All the homes we purchase can close in 10 days, and are all Cash buys. Attached is a flyer that provides the homes that we have bought this year. Please use the same concept of the flyer attached. Company logo attached. 8 x 11 flyer. At the bottom of the flyer we this in small text: "This is not intended to be a solicitation if your home is currently listed with a broker". Please use all the same contact information of the flyer attached. File 17 is another flyer with the address we have purchased this year more clearly visible.
Target Market(s)
Homeowner that need to sell fast.
Industry/Entity Type
Purchase
Font styles to use
Requirements
Must have
- At the bottom of the flyer we this in small text: "This is not intended to be a solicitation if your home is currently listed with a broker"

```html
<!DOCTYPE html>
<html lang="en">
<head>
<meta charset="utf-8">
<title>We Will Buy Your Home – Flyer</title>
<link rel="stylesheet" href="https://fonts.googleapis.com/css2?family=Roboto+Condensed:wght@400;700;900&family=Roboto:wght@400;700&display=swap">
<style>
  :root {
    --red: #e31b23;
    --red-dark: #b3121a;
    --black: #111111;
    --white: #ffffff;
    --sky-top: #3d8fd6;
    --sky-bottom: #e9f4fc;
    --grey-text: #5a5a5a;
    --stage: #d6d6d6;
    --green: #4f8a2a;
  }
  * { box-sizing: border-box; margin: 0; padding: 0; }
  html, body { width: 1200px; height: 1000px; overflow: hidden; }
  body { background: var(--stage); font-family: "Roboto", Arial, sans-serif; position: relative; }

  .flyer {
    position: absolute; left: 293px; top: 78px; width: 614px; height: 844px;
    background: linear-gradient(180deg, var(--sky-top) 0px, #8cc2ec 90px, var(--sky-bottom) 150px, var(--white) 260px, #e6f2fb 400px, var(--white) 470px);
    overflow: hidden;
  }

  .leaves { position: absolute; left: 0; top: 0; width: 120px; height: 110px;
    background: radial-gradient(ellipse at 30% 30%, #9ccc3c, rgba(156,204,60,0) 70%); }

  .brand { position: absolute; left: 66px; top: 84px; display: flex; align-items: center; gap: 6px; z-index: 2; }
  .brand-mark { width: 12px; height: 12px; background: var(--black); }
  .brand-name { font-family: "Roboto Condensed", Arial, sans-serif; font-weight: 700; font-size: 15px; color: var(--black); text-transform: uppercase; white-space: nowrap; }

  .headline { position: absolute; left: 209px; top: 38px; width: 390px; font-family: "Roboto Condensed", Arial, sans-serif; font-weight: 700; text-transform: uppercase; z-index: 2; white-space: nowrap; }
  .headline .lead { font-size: 19.5px; line-height: 22px; color: var(--black); display: block; }
  .headline .big { font-size: 36px; line-height: 32px; color: var(--red); display: block; letter-spacing: -0.3px; }
  .headline .in { font-size: 18px; color: var(--black); letter-spacing: 0; }

  .house-photo { position: absolute; left: 0; top: 126px; width: 614px; height: 146px;
    background: linear-gradient(180deg, #bcd9ef 0%, #d8c9b3 35%, #c9b59a 70%, #dedad2 100%); }

  .steps { position: absolute; left: 39px; top: 269px; width: 536px; height: 168px; }
  .step { position: absolute; top: 0; width: 170px; height: 168px;
    background: linear-gradient(180deg, var(--red) 0%, var(--red-dark) 100%);
    box-shadow: 0 6px 10px rgba(0,0,0,0.25);
    color: var(--white); text-align: center; font-weight: 700; font-size: 11px; line-height: 1.25; }
  .step-1 { left: 0; } .step-2 { left: 183px; } .step-3 { left: 366px; }
  .step-icon { position: absolute; left: 0; right: 0; top: 12px; height: 100px; display: flex; justify-content: center; align-items: center; }
  .step-3 .step-icon { top: 6px; height: 64px; }
  .step-text { position: absolute; left: 6px; right: 6px; bottom: 12px; }
  .step-arrow { position: absolute; top: 72px; right: -10px; width: 0; height: 0;
    border-top: 10px solid transparent; border-bottom: 10px solid transparent; border-left: 10px solid var(--red); z-index: 2; }

  .purchased { position: absolute; left: 40px; top: 467px; width: 540px; height: 300px; }
  .purchased-bar { position: absolute; left: 0; top: 0; width: 14px; height: 293px; background: var(--red-dark); border-radius: 7px 7px 0 0; }
  .purchased-banner { position: absolute; left: 14px; top: 12px; width: 430px; height: 52px; }
  .purchased-banner svg { position: absolute; inset: 0; }
  .purchased-title { position: absolute; left: 20px; top: 8px; font-family: "Roboto Condensed", Arial, sans-serif; font-weight: 700; font-size: 21px; color: var(--white); text-transform: uppercase; white-space: nowrap; }
  .purchased-sub { position: absolute; left: 20px; top: 34px; font-size: 9.5px; font-weight: 700; color: var(--white); white-space: nowrap; }

  .home-list { position: absolute; list-style: none; font-family: "Roboto Condensed", Arial, sans-serif; font-size: 8.3px; color: var(--black); line-height: 9.75px; width: 138px; }
  .home-list.col-a { left: 35px; top: 77px; }
  .home-list.col-b { left: 292px; top: 77px; }
  .home-list li { display: flex; white-space: nowrap; }
  .home-list .num { width: 15px; flex: none; }
  .home-list .street { flex: 1; overflow: hidden; }
  .home-list .street::after { content: " ............................................"; }
  .home-list .price { flex: none; }

  .home-photo { position: absolute; width: 96px; height: 90px; border: 3px solid #d0d0d0; background: linear-gradient(180deg, #79b1e0 0%, #b9d6ec 40%, #c99f78 60%, #d9cfc0 100%); }
  .photo-a { left: 182px; top: 80px; } .photo-b { left: 182px; top: 175px; }
  .photo-c { left: 439px; top: 80px; } .photo-d { left: 439px; top: 175px; }

  .disclaimer { position: absolute; left: 40px; top: 750px; width: 540px; text-align: center; font-size: 9.6px; color: var(--grey-text); text-transform: uppercase; letter-spacing: 0.5px; white-space: nowrap; }

  .footer { position: absolute; left: 0; top: 767px; width: 614px; height: 77px; }
  .footer svg { position: absolute; inset: 0; }
  .footer-address { position: absolute; left: 40px; top: 14px; font-size: 14px; color: var(--white); text-transform: uppercase; white-space: nowrap; }
  .footer-cta { position: absolute; left: 40px; top: 41px; font-size: 10.5px; color: var(--white); text-transform: uppercase; line-height: 1.35; white-space: nowrap; }
  .footer-phone { position: absolute; left: 192px; top: 37px; font-family: "Roboto", Arial, sans-serif; font-weight: 700; font-size: 27px; color: var(--red); white-space: nowrap; }

  .partners { position: absolute; left: 450px; top: 8px; width: 160px; height: 66px; font-family: "Roboto Condensed", Arial, sans-serif; font-weight: 700; }
  .partner { position: absolute; display: flex; align-items: center; gap: 4px; white-space: nowrap; }
  .partner-dot { width: 8px; height: 8px; flex: none; }
  .partner-lease { left: 0; top: 2px; font-size: 12px; color: var(--black); }
  .partner-lease .partner-dot { background: var(--green); }
  .partner-capital { left: 0; top: 40px; font-size: 9px; color: var(--green); }
  .partner-capital .partner-dot { background: var(--green); border-radius: 50%; }
  .partner-lending { left: 82px; top: 40px; font-size: 9px; color: var(--black); }
  .partner-lending .partner-dot { background: var(--black); border-radius: 50%; }
</style>
</head>
<body>
<main class="flyer">
  <div class="leaves" role="img" aria-label="Green leaves in the top corner"></div>

  <div class="house-photo" role="img" aria-label="Photo of a single-storey stucco home with double garages and a landscaped front yard"></div>

  <div class="brand">
    <span class="brand-mark"></span>
    <span class="brand-name">Keystone Realty</span>
  </div>

  <h1 class="headline">
    <span class="lead">We will provide you with an offer to</span>
    <span class="big">Purchase your home</span>
    <span class="big"><span class="in">in </span>24 hours guarantee!</span>
  </h1>

  <section class="steps">
    <div class="step step-1">
      <div class="step-icon">
        <svg width="90" height="96" viewBox="0 0 90 96" fill="none" stroke="#fff" stroke-linecap="round">
          <rect x="27" y="14" width="36" height="66" rx="6" stroke-width="5" transform="rotate(-14 45 47)"/>
          <circle cx="51" cy="71" r="3" fill="#fff" stroke="none" transform="rotate(-14 45 47)"/>
          <path d="M14 20 a22 22 0 0 1 14 -12" stroke-width="3.5"/>
          <path d="M7 18 a30 30 0 0 1 18 -16" stroke-width="3.5"/>
          <path d="M76 76 a22 22 0 0 1 -14 12" stroke-width="3.5"/>
          <path d="M83 78 a30 30 0 0 1 -18 16" stroke-width="3.5"/>
        </svg>
      </div>
      <p class="step-text">Give us a call and provide us<br>with your name and address</p>
      <span class="step-arrow"></span>
    </div>
    <div class="step step-2">
      <div class="step-icon">
        <svg width="80" height="90" viewBox="0 0 80 90" fill="none" stroke="#fff" stroke-linecap="round">
          <path d="M14 50 V40 a26 26 0 0 1 52 0 V50" stroke-width="5"/>
          <rect x="8" y="42" width="14" height="22" rx="5" fill="#fff" stroke="none"/>
          <rect x="58" y="42" width="14" height="22" rx="5" fill="#fff" stroke="none"/>
          <path d="M65 64 Q62 80 44 80" stroke-width="4"/>
          <rect x="36" y="76" width="10" height="8" rx="3" fill="#fff" stroke="none"/>
        </svg>
      </div>
      <p class="step-text">One of our associates will give<br>you a call to schedule a walk<br>through of your property.</p>
      <span class="step-arrow"></span>
    </div>
    <div class="step step-3">
      <div class="step-icon">
        <svg width="72" height="54" viewBox="0 0 80 58" fill="none" stroke="#fff" stroke-width="4" stroke-linejoin="round">
          <rect x="4" y="4" width="72" height="50"/>
          <path d="M4 4 L40 34 L76 4"/>
          <path d="M4 54 L30 26 M76 54 L50 26"/>
        </svg>
      </div>
      <p class="step-text">We will email you an offer<br>to purchase within 24 hours<br>of walking your property.<br>All the homes we purchase<br>can close in 10 days,<br>and are all Cash buys</p>
    </div>
  </section>

  <section class="purchased">
    <div class="purchased-bar"></div>
    <div class="purchased-banner">
      <svg viewBox="0 0 430 52" width="430" height="52" preserveAspectRatio="none">
        <polygon points="0,0 406,0 430,26 406,52 0,52" fill="#8a8a8a"/>
        <polygon points="0,2 404,2 426,26 404,50 0,50" fill="#111"/>
      </svg>
      <h2 class="purchased-title">Homes purchased this year (2014):</h2>
      <p class="purchased-sub">All homes purchased in this program by our investors are used for rental purposes.</p>
    </div>

    <ol class="home-list col-a">
      <li><span class="num">1.</span><span class="street">10415 Quail Hollow</span><span class="price">$91,000</span></li>
      <li><span class="num">2.</span><span class="street">12308 Sierra Vista</span><span class="price">$120,000</span></li>
      <li><span class="num">3.</span><span class="street">3174 Coyote Ridge</span><span class="price">$162,500</span></li>
      <li><span class="num">4.</span><span class="street">12657 Morning Star</span><span class="price">$120,000</span></li>
      <li><span class="num">5.</span><span class="street">581 Via Del Sol</span><span class="price">$218,000</span></li>
      <li><span class="num">6.</span><span class="street">3302 Juniper Point</span><span class="price">$98,404</span></li>
      <li><span class="num">7.</span><span class="street">7190 Copper Sky</span><span class="price">$100,000</span></li>
      <li><span class="num">8.</span><span class="street">11468 Cedar Bluff</span><span class="price">$178,000</span></li>
      <li><span class="num">9.</span><span class="street">5617 Luna Vista</span><span class="price">$147,500</span></li>
      <li><span class="num">10.</span><span class="street">11902 Amber Sands</span><span class="price">$86,500</span></li>
      <li><span class="num">11.</span><span class="street">10871 Ranch Hollow</span><span class="price">$118,000</span></li>
      <li><span class="num">12.</span><span class="street">3182 Tierra Alta</span><span class="price">$92,000</span></li>
      <li><span class="num">13.</span><span class="street">3046 Canyon Mesa</span><span class="price">$167,500</span></li>
      <li><span class="num">14.</span><span class="street">11655 Clear Spring</span><span class="price">$83,000</span></li>
      <li><span class="num">15.</span><span class="street">14127 Falcon Ridge</span><span class="price">$86,000</span></li>
      <li><span class="num">16.</span><span class="street">738 Desert Bloom</span><span class="price">$86,800</span></li>
      <li><span class="num">17.</span><span class="street">11913 Palo Verde</span><span class="price">$86,000</span></li>
      <li><span class="num">18.</span><span class="street">11294 Northgate</span><span class="price">$152,000</span></li>
      <li><span class="num">19.</span><span class="street">12019 Rio Grande</span><span class="price">$95,000</span></li>
      <li><span class="num">20.</span><span class="street">12896 Tierra Dorada</span><span class="price">$105,320</span></li>
    </ol>

    <div class="home-photo photo-a" role="img" aria-label="Photo of a purchased single-storey home"></div>
    <div class="home-photo photo-b" role="img" aria-label="Photo of a purchased two-storey home"></div>

    <ol class="home-list col-b" start="21">
      <li><span class="num">21.</span><span class="street">547 Paseo Del Rey</span><span class="price">$119,000</span></li>
      <li><span class="num">22.</span><span class="street">11569 Monte Verde</span><span class="price">$150,000</span></li>
      <li><span class="num">23.</span><span class="street">10583 Silverleaf</span><span class="price">$85,000</span></li>
      <li><span class="num">24.</span><span class="street">3217 Jade Point</span><span class="price">$107,660</span></li>
      <li><span class="num">25.</span><span class="street">709 Sage Brush</span><span class="price">$84,000</span></li>
      <li><span class="num">26.</span><span class="street">12532 Flor Del Sol</span><span class="price">$84,362</span></li>
      <li><span class="num">27.</span><span class="street">14226 Desert Wind</span><span class="price">$80,426</span></li>
      <li><span class="num">28.</span><span class="street">11159 Stone Cove</span><span class="price">$121,500</span></li>
      <li><span class="num">29.</span><span class="street">352 Hillside</span><span class="price">$80,000</span></li>
      <li><span class="num">30.</span><span class="street">6214 Bandera</span><span class="price">$157,000</span></li>
      <li><span class="num">31.</span><span class="street">12318 Tierra Roja</span><span class="price">$81,000</span></li>
      <li><span class="num">32.</span><span class="street">486 Agave Crossing</span><span class="price">$85,000</span></li>
      <li><span class="num">33.</span><span class="street">5503 Pinon Ridge</span><span class="price">$149,000</span></li>
      <li><span class="num">34.</span><span class="street">14239 Mesa Rock</span><span class="price">$101,550</span></li>
      <li><span class="num">35.</span><span class="street">6297 Ocotillo Circle</span><span class="price">$68,298</span></li>
      <li><span class="num">36.</span><span class="street">7958 Starry Fall</span><span class="price">$108,000</span></li>
      <li><span class="num">37.</span><span class="street">12684 Sun Canyon</span><span class="price">$157,000</span></li>
      <li><span class="num">38.</span><span class="street">11483 Adobe Creek</span><span class="price">$138,500</span></li>
      <li><span class="num">39.</span><span class="street">1391 Vista Grande</span><span class="price">$143,500</span></li>
      <li><span class="num">40.</span><span class="street">10792 Pleasant Ridge</span><span class="price">$125,000</span></li>
    </ol>

    <div class="home-photo photo-c" role="img" aria-label="Photo of a purchased two-storey stucco home"></div>
    <div class="home-photo photo-d" role="img" aria-label="Photo of a purchased two-storey brick home"></div>
  </section>

  <p class="disclaimer">This is not intended to be a solicitation if your home is currently listed with a broker</p>

  <footer class="footer">
    <svg viewBox="0 0 614 77" width="614" height="77" preserveAspectRatio="none">
      <rect width="614" height="77" fill="#111"/>
      <polygon points="452,0 614,0 614,77 420,77" fill="#fff"/>
    </svg>
    <p class="footer-address">218 N. Canyon Ridge, B-2 El Paso, TX 79912</p>
    <p class="footer-cta">Call us today to<br>schedule an appointment</p>
    <p class="footer-phone">915-555-0148</p>
    <div class="partners">
      <span class="partner partner-lease"><span class="partner-dot"></span>Desert Lease Homes</span>
      <span class="partner partner-capital"><span class="partner-dot"></span>Mesa Capital LLC</span>
      <span class="partner partner-lending"><span class="partner-dot"></span>Summit Lending</span>
    </div>
  </footer>
</main>
</body>
</html>
```